Interior Design/ New Construction interior finishes

Interior Design Website

Target Market(s)

Home builders, New Construction, Renovations, Public

Industry/Entity Type

Construction

Coding

Coded - Design and coding required

Number of Pages Required

1 page

Font styles to use
Sans Serif

Colors

Designer to choose colors to be used in the design.

Requirements
Must have
• Section to upload pictures of projects
• Simple and modern design
• Designer 1 details about myself
• Logo
• Upload section for photos for future jobs
Nice to have
• Sections they can click on to see certain rooms in a house
• Decorating, floral arrangements, holiday decorating.
• I have lots of before and after as well. Maybe a section for those.

```html
<!DOCTYPE html>
<html lang="en">
<head>
<meta charset="utf-8">
<title>Lumen Interiors</title>
<link href="https://fonts.googleapis.com/css2?family=Lato:wght@300;400;700;900&display=swap" rel="stylesheet">
<style>
:root{
  --ink:#1f1f1f;
  --text:#333;
  --muted:#666;
  --paper:#f4f4f4;
  --white:#fff;
  --line:#cfcfcf;
  --dark:#1c1c1c;
  --overlay:rgba(20,20,20,.62);
  --card:#ececec;
}
*{box-sizing:border-box;margin:0;padding:0}
html,body{width:1200px;height:3622px;overflow:hidden}
body{font-family:'Lato',sans-serif;color:var(--text);background:var(--paper)}
.wrap{width:960px;margin:0 auto;position:relative}
section,header,footer{position:relative;overflow:hidden}

/* header */
.site-header{height:155px;background:var(--paper)}
.brand{position:absolute;left:121px;top:24px;text-align:center;width:180px}
.brand-mark{width:76px;height:76px;border:3px solid var(--ink);border-radius:50%;margin:0 auto}
.brand-name{font-size:22px;letter-spacing:2px;color:var(--ink);margin-top:6px;font-weight:400}
.contact-top{position:absolute;right:121px;top:26px;display:flex;gap:34px;font-size:14px;color:var(--muted)}
.contact-top span{display:flex;align-items:center;gap:9px}
.contact-top svg{width:20px;height:20px}
.main-nav{position:absolute;right:121px;top:113px;display:flex;gap:0}
.main-nav a{font-size:12.5px;color:var(--ink);text-decoration:none;padding:0 15px;height:42px;line-height:20px;text-transform:uppercase;position:relative}
.main-nav a.active::after{content:"";position:absolute;left:15px;right:15px;top:26px;height:16px;background:var(--ink)}

/* hero */
.hero{height:565px;background:linear-gradient(180deg,#d9d6d0 0%,#bdb5a8 45%,#8f7e6a 75%,#7b8694 100%)}
.slide-btn{position:absolute;top:252px;width:46px;height:46px;display:flex;align-items:center;justify-content:center}
.slide-btn.prev{left:0;background:var(--white)}
.slide-btn.next{right:0;background:var(--ink)}
.dots{position:absolute;left:0;right:0;display:flex;justify-content:center;gap:8px}
.hero .dots{top:530px}
.dot{width:10px;height:10px;border-radius:50%;border:2px solid var(--white);background:transparent}
.dot.on{background:var(--white)}

/* headings */
.sec-title{font-size:36px;font-weight:400;color:var(--ink);text-align:center;letter-spacing:.5px}
.sec-sub{font-size:16px;font-weight:700;text-align:center;color:var(--ink);margin-top:10px}
.btn{display:inline-block;border:2px solid #444;font-size:13px;color:var(--ink);padding:4px 14px;background:var(--white)}
.btn.light{border-color:var(--white);color:var(--white);background:transparent}

/* services */
.services{height:378px;background:var(--paper);padding-top:48px}
.service-row{display:flex;margin-top:60px}
.service{width:380px}
.service h3{font-size:23px;font-weight:400;color:var(--ink);line-height:29px;width:260px}
.service p{font-size:12.5px;color:var(--muted);line-height:17px;width:240px;margin:10px 0 12px}

/* about */
.about{height:295px;background:linear-gradient(90deg,#5d5c5a,#8a8682 50%,#4d4a46)}
.about .shade,.features .shade,.site-footer .shade{position:absolute;inset:0;background:var(--overlay)}
.about .inner{position:relative;text-align:center;color:var(--white);padding-top:84px}
.about h2{font-size:38px;font-weight:700}
.about p{font-size:16px;font-weight:700;margin:12px 0 20px}

/* projects */
.projects{height:526px;background:var(--paper);padding-top:38px}
.project-strip{display:flex;margin-top:38px;height:242px}
.project-strip div{flex:1}
.projects .more{text-align:center;margin-top:52px}

/* features */
.features{height:299px;background:linear-gradient(90deg,#3a2f29,#5c4a3e 50%,#2f2a27)}
.feature-row{position:relative;display:flex;justify-content:center;gap:0;padding-top:68px}
.feature{width:326px;text-align:center;color:var(--white)}
.feature svg{width:42px;height:42px}
.feature h3{font-size:28px;font-weight:700;margin-top:8px}
.feature p{font-size:14px;line-height:17px;width:200px;margin:6px auto 0}
.read{font-size:13.5px;display:inline-flex;align-items:center;gap:4px}
.read i{display:inline-block;width:13px;height:13px;border:1px solid currentColor;border-radius:50%}

/* blogs */
.blogs{height:708px;background:var(--white);padding-top:40px}
.blog-row{display:flex;gap:15px;margin-top:44px;padding-left:2px}
.post{width:313px;height:441px;background:var(--card)}
.post:nth-child(2){width:305px}
.post.featured{background:var(--dark);border:7px solid var(--dark);color:var(--white)}
.post .thumb{height:230px}
.post .body{padding:14px 20px}
.post .meta{font-size:11.5px;line-height:15px}
.post h4{font-size:18px;font-weight:700;margin:8px 0 12px}
.post p{font-size:13px;line-height:16px}
.post .read{margin-top:10px}
.blogs .dots{position:static;margin-top:32px}
.blogs .dot{border-color:#999}
.blogs .dot.on{background:var(--ink);border-color:var(--ink)}
.blogs .more{text-align:center;margin-top:26px}

/* newsletter */
.newsletter{height:253px;background:var(--paper);padding-top:74px}
.sub-form{display:flex;width:565px;margin:22px auto 0;height:46px}
.sub-form .field{flex:1;border:1px solid #aaa;background:var(--white);font-size:12.5px;color:#999;padding:0 18px;line-height:44px}
.sub-form .send{width:74px;background:var(--ink);display:flex;align-items:center;justify-content:center}

/* footer */
.site-footer{height:443px;background:linear-gradient(90deg,#2a2622,#4a4038 50%,#231f1c)}
.site-footer .inner{position:relative;color:var(--white);width:960px;margin:0 auto;height:100%}
.f-top{position:absolute;top:58px;left:2px;right:0;height:90px}
.f-col h5{font-size:18px;font-weight:700;margin-bottom:6px}
.f-col p{font-size:15px;line-height:19px}
.vline{position:absolute;top:4px;width:3px;height:62px;background:var(--white)}
.hline{position:absolute;left:2px;right:0;height:1px;background:rgba(255,255,255,.7)}
.social{display:flex;gap:8px;justify-content:center;margin-top:10px}
.social span{width:32px;height:32px;border:2px solid var(--white);border-radius:50%}
.f-sub{display:flex;margin-top:10px;height:30px;width:294px}
.f-sub .field{flex:1;background:var(--white);color:#555;font-size:12px;line-height:30px;padding-left:10px}
.f-sub .send{width:46px;background:var(--ink);display:flex;align-items:center;justify-content:center}
.copy{position:absolute;top:402px;left:2px;right:0;display:flex;justify-content:space-between;font-size:12px}
.copy nav{display:flex;gap:20px;text-transform:uppercase}
</style>
</head>
<body>

<header class="site-header">
  <div class="brand">
    <div class="brand-mark"></div>
    <div class="brand-name">Lumen Interiors</div>
  </div>
  <div class="contact-top">
    <span><svg viewBox="0 0 20 20"><circle cx="10" cy="10" r="8.5" fill="none" stroke="#555" stroke-width="1.5"/><path d="M6.5 6.5l2 0 1 2-1.2 1a5 5 0 0 0 2.2 2.2l1-1.2 2 1v2a6.5 6.5 0 0 1-7-7z" fill="#555"/></svg>202-555-0143</span>
    <span><svg viewBox="0 0 20 20"><circle cx="10" cy="10" r="8.5" fill="none" stroke="#555" stroke-width="1.5"/><path d="M6 13l6-6m-6 6l1-3m-1 3l3-1" stroke="#555" stroke-width="1.5" fill="none"/></svg>hello@lumeninteriors.com</span>
  </div>
  <nav class="main-nav">
    <a class="active">Home</a><a>About</a><a>What We Do</a><a>Projects</a><a>Pages</a><a>Blogs</a><a>Contact Us</a>
  </nav>
</header>

<section class="hero" role="img" aria-label="Photo of a bright living room with white sofas and a rustic wooden coffee table">
  <div class="slide-btn prev"><svg width="18" height="22" viewBox="0 0 18 22"><path d="M4 2l10 9-10 9" fill="none" stroke="#1f1f1f" stroke-width="4"/></svg></div>
  <div class="slide-btn next"><svg width="18" height="22" viewBox="0 0 18 22"><path d="M14 2L4 11l10 9" fill="none" stroke="#fff" stroke-width="4"/></svg></div>
  <div class="dots"><span class="dot on"></span><span class="dot"></span><span class="dot"></span></div>
</section>

<section class="services">
  <h2 class="sec-title">What We Do</h2>
  <div class="wrap service-row">
    <div class="service"><h3>Complete Design Package</h3><p>Lorem Ipsum is simply dummy text of the printing and typesetting industry.</p><span class="btn">Read More</span></div>
    <div class="service"><h3>Home Styling and Personal Shopping</h3><p>Lorem Ipsum is simply dummy text of the printing and typesetting industry.</p><span class="btn">Read More</span></div>
    <div class="service"><h3>Turnkey Design Package</h3><p>Lorem Ipsum is simply dummy text of the printing and typesetting industry.</p><span class="btn">Read More</span></div>
  </div>
</section>

<section class="about" role="img" aria-label="Photo of a white kitchen with dark wood floor">
  <div class="shade"></div>
  <div class="inner">
    <h2>About Us</h2>
    <p>Lorem Ipsum is simply dummy text of the printing and typesetting industry.</p>
    <span class="btn light">Read More</span>
  </div>
</section>

<section class="projects">
  <h2 class="sec-title" style="font-weight:700">Projects</h2>
  <p class="sec-sub">Lorem Ipsum is simply dummy text of the printing and typesetting industry.</p>
  <div class="project-strip">
    <div role="img" aria-label="Dining room with wooden beams" style="background:linear-gradient(#8a6a4a,#c9b59a)"></div>
    <div role="img" aria-label="Dark home theatre room" style="background:linear-gradient(#2e2a2a,#5a2323)"></div>
    <div role="img" aria-label="Bathroom with freestanding tub" style="background:linear-gradient(#d8d4cf,#a9a39b)"></div>
    <div role="img" aria-label="White kitchen sink with black faucet" style="background:linear-gradient(#e4e2df,#6f6b66)"></div>
    <div role="img" aria-label="Living room with stone fireplace" style="background:linear-gradient(#b08a5c,#7a5a3c)"></div>
  </div>
  <div class="more"><span class="btn">View More</span></div>
</section>

<section class="features" role="img" aria-label="Photo of a bedroom with upholstered bed">
  <div class="shade"></div>
  <div class="feature-row">
    <div class="feature">
      <svg viewBox="0 0 42 42"><path d="M4 20L21 5l17 15v18H4z" fill="none" stroke="#fff" stroke-width="3"/><path d="M12 22h18M12 28h18M12 34h18" stroke="#fff" stroke-width="3"/></svg>
      <h3>Designs</h3><p>Lorem Ipsum is simply dummy text of the printing and typesetting industry.</p><span class="read">Read More... <i></i></span>
    </div>
    <div class="feature">
      <svg viewBox="0 0 42 42"><path d="M21 10a9 9 0 0 0-5 16.5V31h10v-4.5A9 9 0 0 0 21 10z" fill="none" stroke="#fff" stroke-width="2.5"/><path d="M17 35h8M21 2v4M6 9l3 3M36 9l-3 3M2 20h4M36 20h4" stroke="#fff" stroke-width="2.5"/></svg>
      <h3>Ideas</h3><p>Lorem Ipsum is simply dummy text of the printing and typesetting industry.</p><span class="read">Read More... <i></i></span>
    </div>
    <div class="feature">
      <svg viewBox="0 0 42 42"><path d="M4 12h9l3-5h10l3 5h9v24H4z" fill="none" stroke="#fff" stroke-width="3"/><circle cx="21" cy="23" r="7" fill="none" stroke="#fff" stroke-width="3"/></svg>
      <h3>Decoration</h3><p>Lorem Ipsum is simply dummy text of the printing and typesetting industry.</p><span class="read">Read More... <i></i></span>
    </div>
  </div>
</section>

<section class="blogs">
  <h2 class="sec-title">Blogs</h2>
  <div class="wrap blog-row">
    <article class="post featured">
      <div class="thumb" role="img" aria-label="Dining table with grey upholstered chairs" style="background:linear-gradient(#e9e7e3,#9c9a96)"></div>
      <div class="body"><div class="meta">Feb 19,2018<br>By &nbsp;DANIEL MOSS</div><h4>LOREAM IPSUM</h4><p>Lorem Ipsum is simply dummy text of the printing and typesetting industry. Lorem Ipsum has been the industry's standard dummy text.</p><div class="read">Read More... <i></i></div></div>
    </article>
    <article class="post">
      <div class="thumb" role="img" aria-label="Wooden dining table and bench" style="background:linear-gradient(#dedbd6,#8f7a66)"></div>
      <div class="body"><div class="meta">Feb 19,2018<br>By &nbsp;DANIEL MOSS</div><h4>LOREAM IPSUM</h4><p>Lorem Ipsum is simply dummy text of the printing and typesetting industry. Lorem Ipsum has been the industry's standard dummy text.</p><div class="read">Read More... <i></i></div></div>
    </article>
    <article class="post">
      <div class="thumb" role="img" aria-label="Coffee table styled with flowers and books" style="background:linear-gradient(#e4e1de,#a38d73)"></div>
      <div class="body"><div class="meta">Feb 19,2018<br>By &nbsp;DANIEL MOSS</div><h4>LOREAM IPSUM</h4><p>Lorem Ipsum is simply dummy text of the printing and typesetting industry. Lorem Ipsum has been the industry's standard dummy text.</p><div class="read">Read More... <i></i></div></div>
    </article>
  </div>
  <div class="dots"><span class="dot on"></span><span class="dot"></span><span class="dot"></span></div>
  <div class="more"><span class="btn">View More</span></div>
</section>

<section class="newsletter">
  <h2 class="sec-title">Subscribe For Our Newsletter</h2>
  <div class="sub-form">
    <div class="field">Your E-mail Here</div>
    <div class="send"><svg width="24" height="22" viewBox="0 0 24 22"><path d="M1 10L23 1 17 21l-5-7z" fill="#fff"/></svg></div>
  </div>
</section>

<footer class="site-footer" role="img" aria-label="Photo of a staircase and hallway">
  <div class="shade"></div>
  <div class="inner">
    <div class="f-top">
      <div class="f-col" style="position:absolute;left:0"><h5>Call Us Now</h5><p>202-555-0143</p></div>
      <div class="vline" style="left:263px"></div>
      <div class="f-col" style="position:absolute;left:393px"><h5>Come Visit Us</h5><p>48 Harbor Ave. Easton,<br>FL 32011</p></div>
      <div class="vline" style="left:693px"></div>
      <div class="f-col" style="position:absolute;right:0;text-align:right"><h5>Send Massage</h5><p>hello@lumeninteriors.com</p></div>
    </div>
    <div class="hline" style="top:155px"></div>
    <div class="f-col" style="position:absolute;left:2px;top:192px;width:200px">
      <div style="width:50px;height:50px;border:2px solid #fff;border-radius:50%;margin-left:32px"></div>
      <p style="font-size:15px;letter-spacing:1px;margin:4px 0 6px">Lumen Interiors</p>
      <p style="font-size:13px;line-height:16px">Lorem Ipsum is simply dummy text of the printing and typesetting industry.</p>
      <p class="read" style="font-size:13px;margin-top:8px">Read More... <i></i></p>
    </div>
    <div class="f-col" style="position:absolute;left:418px;top:200px;width:140px;text-align:center">
      <h5>Follow Us</h5>
      <div class="social"><span></span><span></span><span></span></div>
    </div>
    <div class="f-col" style="position:absolute;right:0;top:200px;width:294px">
      <h5>Subscribe Now</h5>
      <div class="f-sub"><div class="field">E-Mail</div><div class="send"><svg width="16" height="15" viewBox="0 0 24 22"><path d="M1 10L23 1 17 21l-5-7z" fill="#fff"/></svg></div></div>
    </div>
    <div class="hline" style="top:382px"></div>
    <div class="copy">
      <span>CopyRight © 2018 Lumen Interiors. All Right Reserve</span>
      <nav><span>Home</span><span>About</span><span>What We Do</span><span>Projects</span><span>Pages</span><span>Blogs</span><span>Contact Us</span></nav>
    </div>
  </div>
</footer>

</body>
</html>
```